Flower delivery business needs sales brochure

I have a courier business that specialises in same-day flower deliveries; I want to make a single page A4 sales brochure (folded to DL) to give to our potential customers.
The company website is petalvanto.com, this will give an idea of who we are and what we do, as well as some graphics and colours that we use.
When opened, the inside A4 space of the brochure will be a pricelist, so the entire page will be an excel table with delivery locations and prices; we will add the prices ourselves later, so ideally the inside will be a background of some sort that won't obstruct text. Maybe light/transparent flowers and a background colour?
The front of the DL brochure should be mostly a title page, so business name, phone number, a graphic?
The first inside page should relate to our service, there's a lot of info on our website that you could use, so same day delivery, 10:30 and 2:30 pick-up times, established over 10 years ago, air-conditioned vans, delivery to 300+ suburbs.
The back page would be contact details and maybe a summary of the key points of the 'about us' section of the website.

Industry/Entity Type

Business

```html
<!DOCTYPE html>
<html lang="en">
<head>
<meta charset="utf-8">
<title>Petal Vanto – Service Panel</title>
<link rel="stylesheet" href="https://fonts.googleapis.com/css2?family=Open+Sans:ital,wght@0,400;0,700;1,400;1,600&family=Lora:ital,wght@1,600&display=swap">
<style>
:root{
  --orange:#f07b1c;
  --orange-deep:#e0661a;
  --ink:#3b3b3b;
  --paper:#ffffff;
  --peach:#fde3c8;
  --bloom:#f3a24c;
  --leaf:#8fb35a;
}
*{box-sizing:border-box;margin:0;padding:0}
html,body{width:849px;height:1200px;overflow:hidden;background:var(--paper)}
.panel{
  position:relative;width:849px;height:1200px;overflow:hidden;
  font-family:"Open Sans",Arial,sans-serif;color:var(--ink);
  background:linear-gradient(180deg,var(--paper) 0%,var(--paper) 52%,#fff4ea 68%,var(--peach) 80%,var(--bloom) 100%);
}
.column{position:absolute;top:22px}
.column--left{left:40px;width:385px}
.column--right{left:448px;width:370px}
.heading{font-weight:700;color:var(--orange);font-size:27px;line-height:1.2;margin-bottom:14px}
.subheading{font-style:italic;font-weight:600;color:var(--orange);font-size:20px;margin:-4px 0 8px}
.body{font-size:19.5px;line-height:1.48;margin-bottom:14px}
.accent{color:var(--orange);font-style:italic}
.bullets{list-style:none;margin:0 0 14px 0}
.bullets li{position:relative;padding-left:20px;font-size:19.5px;line-height:1.48;margin-bottom:8px}
.bullets li::before{content:"";position:absolute;left:3px;top:12px;width:7px;height:7px;border-radius:50%;background:var(--orange)}
.section-gap{margin-top:26px}
.photo-flowers-left{
  position:absolute;left:0;top:900px;width:450px;height:300px;
  background:radial-gradient(ellipse at 40% 40%,#f6a04f 0%,#ee8a33 45%,rgba(240,123,28,0) 80%);
  opacity:.55;
}
.photo-gift{
  position:absolute;left:480px;top:500px;width:369px;height:700px;
  background:linear-gradient(160deg,#f9d27a 0%,#f29a3f 35%,#e86b50 60%,#f4c6a2 85%,#f7e0cc 100%);
  border-radius:40px 0 0 0;
}
.promise{
  position:absolute;left:40px;top:948px;width:390px;
  font-family:"Lora",Georgia,serif;font-style:italic;font-weight:600;
  color:var(--paper);font-size:22px;line-height:1.38;
}
.brand{position:absolute;left:22px;top:1112px;display:flex;align-items:center;gap:12px}
.brand__mark{width:44px;height:44px;border-radius:50%;background:var(--orange-deep)}
.brand__name{font-weight:700;font-size:34px;color:var(--paper);letter-spacing:1px;line-height:1}
.brand__tagline{position:absolute;left:132px;top:1152px;font-style:italic;font-size:17px;color:var(--paper)}
</style>
</head>
<body>
<main class="panel">
  <div class="photo-flowers-left" role="img" aria-label="Soft bouquet of orange flowers behind the service summary"></div>
  <div class="photo-gift" role="img" aria-label="Colourful flower bouquet with balloons, a teddy bear and a smiling woman holding flowers"></div>

  <section class="column column--left">
    <h2 class="heading">Pickup &amp; Delivery Times</h2>
    <p class="body">Our service offers pick-ups twice a day for those florists whose volume requires it:</p>
    <ul class="bullets">
      <li>a mid-morning pick-up prior to our depot <span class="accent">handover at 11:30 noon</span></li>
      <li>an afternoon pickup prior to our second depot <span class="accent">handover at 2:30pm</span></li>
    </ul>
    <p class="body">Most flowers are delivered within 4/5 hours after pick-up. Local (ie within area of pickup location) and timed deliveries are given priority and we can accommodate for special deadlines with prior notice.</p>

    <h2 class="heading section-gap">Delivery Areas</h2>
    <p class="body">We work on a system to ensure that your flowers spend the minimum amount of time in transit as possible. As such, we encourage our customers to supply orders for outlying areas (indicated in blue) to be picked up on the afternoon run, provided they can be delivered after 5:00pm. Most special order requirements can be accommodated with prior notice.</p>
  </section>

  <section class="column column--right">
    <h2 class="heading">Pricing &amp; Surcharges</h2>
    <p class="subheading">What makes us different ?</p>
    <p class="body">All price lists are customized for each customer based on location of pickup and volume per week. Please contact us and we will be happy to provide a price list based on the information you provide. Unlike other couriers, our surcharges are kept at an absolute minimum - we don't charge for additional items that accompany an order (eg balloons, chocolates or teddy bears*). We also will not charge for a timed delivery that can be done within the driver's daily run or is provided the day before.</p>
  </section>

  <p class="promise">You could use, so same day delivery, 10:30 and 2:30 pick-up times, established over 10 years ago, air-conditioned vans, delivery to 300+ suburbs.</p>

  <div class="brand">
    <span class="brand__mark"></span>
    <span class="brand__name">PETAL VANTO</span>
  </div>
  <p class="brand__tagline">Florist Delivery Service</p>
</main>
</body>
</html>
```